Flyer Needed to Advertise New Online Reading Programs

ABOUT THE ACADEMY OF LITERACY GROWTH
The Institute teaches summer reading skills programs for elementary school students, in programs offered through partnerships with universities, colleges and municipalities nationwide. The goal of each program is to build reading skills, and to foster a lifetime love of books and reading.

AIMS & TARGET MARKET
The Institute has developed a new format of its’ online reading program for elementary students, which includes live small-group video classes taught by a professional reading teacher. The Institute seeks a new graphic design for a flyer to advertise the new online reading program. The flyer will be sent to elementary schools, passed out by teachers, and then taken home by students to show parents; therefore, the primary audience for the flyer will be teachers and parents of elementary school students.

Live classes for children are completely new in online education, unlike anything else in the marketplace, and parents and teachers therefore have no experience with them. The successful design will include illustrations or photographs that allow visitors to immediately grasp/understand the new video class format, without relying heavily on a written description. Additionally, the successful flyer concept will make the program, and the video classes in particular, feel fun and appealing to kids and parents.

Below is additional information about the new live small-group video class format, which meets weekly for 6 weeks:
o During video classes, students participate from home.
o During discussions, the student’s computer (or tablet) screen is filled with live video frames of the teacher and the other students. The video frame for the teacher is larger, and the other students appear in smaller frames.
o During other video class instruction, the teacher uses a presentation screen to display pages of a book or a “whiteboard” used for instructional activities.

Notes: The flyer design could include an illustrated or photo screenshot of a video class, with children looking engaged and a teacher leading them in discussion (stock photos are okay to use in flyer design). We have included a screen shot of one of these classes for reference, but do not feel constrained to represent this screen realistically (as shown here). Layout, look and feel can be changed. Alternatively, you may choose to use a graphic other than a screenshot to bring across the concept of the video classes.

COPY AND SPECIFICATIONS
The flyer design will be one-sided and the dimensions are 8.5” x 11” in either portrait or landscape orientation. We will consider designs in color or black and white. Since we brand our flyers with logos of the universities we partner with throughout the nation, we’ll need to include a partner logo in the design. Exact copy will be provided, but layout is flexible. Screenshots from our sample classes are included to show screen layout. Stock photos are okay to use in flyer designs.

Hi designers, We wanted to share our thoughts on the main image of the flyer. We're leaning towards an image that shows a sole student on a computer with the computer screen in view. The computer screen could have the sample image we provided to show how the video classes operate. Thanks! The Academy of Literacy Growth

```html
<!DOCTYPE html>
<html lang="en">
<head>
<meta charset="utf-8">
<title>Reading Skills Classes Online this Summer – Flyer</title>
<link rel="stylesheet" href="https://fonts.googleapis.com/css2?family=Chewy&family=Comic+Neue:wght@400;700&family=Libre+Baskerville:wght@400;700&family=Arimo:wght@400;700&family=Questrial&display=swap">
<style>
  :root {
    --ink: #1c1c1c;
    --paper: #ffffff;
    --cloud: #d6d6d6;
    --body-text: #555555;
    --footer-curve: #9a9a9a;
  }
  * { margin: 0; padding: 0; box-sizing: border-box; }
  html, body { width: 939px; height: 1200px; overflow: hidden; background: var(--paper); }
  .flyer { position: relative; width: 939px; height: 1200px; overflow: hidden; background: var(--paper); font-family: "Questrial", sans-serif; }
  .flyer__backdrop { position: absolute; inset: 0; }

  .partner-name {
    position: absolute; left: 40px; top: 66px; width: 220px;
    display: flex; align-items: center; gap: 12px;
    font-family: "Questrial", sans-serif; font-weight: 400; color: var(--paper);
    font-size: 25px; line-height: 1.15;
  }
  .partner-name__mark { width: 22px; height: 22px; background: var(--paper); flex: none; }

  .headline {
    position: absolute; left: 276px; top: 44px; width: 640px; white-space: nowrap;
    font-family: "Chewy", cursive; font-weight: 400; font-size: 30px; color: var(--paper);
    -webkit-text-stroke: 1px var(--ink); paint-order: stroke fill;
    text-shadow: 2px 2px 0 var(--ink); letter-spacing: 0.3px;
  }
  .features { position: absolute; list-style: none; font-family: "Comic Neue", cursive; font-weight: 700; font-size: 17px; color: var(--ink); line-height: 1.2; white-space: nowrap; }
  .features li { height: 29px; }
  .features li::before { content: "\2732\00a0"; }
  .features--left { left: 278px; top: 100px; }
  .features--right { left: 610px; top: 100px; }
  .features--right li.features__indent { height: 24px; margin-top: -6px; padding-left: 20px; }
  .features--right li.features__indent::before { content: ""; }

  .skills-title { position: absolute; left: 43px; top: 184px; font-family: "Libre Baskerville", serif; font-weight: 700; font-size: 16px; color: var(--paper); }
  .skills { position: absolute; left: 43px; top: 216px; list-style: none; font-family: "Comic Neue", cursive; font-size: 20px; color: var(--paper); }
  .skills li { display: flex; align-items: center; gap: 8px; height: 33px; }
  .skills svg { width: 18px; height: 18px; flex: none; }

  .photo { position: absolute; border: 2px solid var(--paper); }
  .photo--a { left: 292px; top: 230px; width: 118px; height: 84px; background: linear-gradient(135deg, #e4e4e4, #8a8a8a); }
  .photo--b { left: 292px; top: 337px; width: 118px; height: 99px; background: linear-gradient(160deg, #f0f0f0, #7a7a7a); }
  .photo--c { left: 765px; top: 230px; width: 136px; height: 92px; background: linear-gradient(135deg, #9a9a9a, #e8e8e8); }
  .photo--d { left: 765px; top: 347px; width: 136px; height: 90px; background: linear-gradient(200deg, #dcdcdc, #555555); }

  .monitor { position: absolute; left: 450px; top: 230px; width: 297px; height: 263px; }
  .monitor__screen { position: absolute; left: 22px; top: 18px; width: 253px; height: 190px; background: linear-gradient(150deg, #d8d8d8 0%, #9c9c9c 55%, #4a4a4a 100%); }

  .programs-title { position: absolute; left: 43px; top: 474px; font-family: "Arimo", sans-serif; font-weight: 700; font-size: 16px; color: var(--ink); }
  .programs { position: absolute; left: 70px; top: 512px; width: 801px; }
  .program { height: 77px; }
  .program--tall { height: 94px; }
  .program h2 { font-family: "Arimo", sans-serif; font-weight: 700; font-size: 14px; color: var(--ink); margin-bottom: 4px; line-height: 18px; }
  .program p { font-family: "Arimo", sans-serif; font-size: 11.4px; line-height: 15px; color: var(--body-text); text-align: justify; text-align-last: left; }

  .contact { position: absolute; left: 50px; top: 1114px; font-family: "Libre Baskerville", serif; color: var(--paper); font-size: 19px; }
  .contact__phone { position: absolute; left: 50px; top: 1160px; display: flex; align-items: center; gap: 4px; font-family: "Arimo", sans-serif; font-weight: 700; color: var(--paper); font-size: 22px; }
  .contact__phone svg { width: 22px; height: 22px; }
  .schedule-note { position: absolute; left: 518px; top: 1136px; font-family: "Arimo", sans-serif; color: var(--paper); font-size: 15px; }
  .hours { position: absolute; left: 452px; top: 1166px; font-family: "Arimo", sans-serif; font-weight: 700; color: var(--paper); font-size: 15px; }
</style>
</head>
<body>
<main class="flyer">
  <svg class="flyer__backdrop" width="939" height="1200" viewBox="0 0 939 1200" aria-hidden="true">
    <defs>
      <linearGradient id="header-fill" x1="0" y1="0" x2="0" y2="1">
        <stop offset="0" stop-color="#5e5e5e"/>
        <stop offset="0.6" stop-color="#8a8a8a"/>
        <stop offset="1" stop-color="#b5b5b5"/>
      </linearGradient>
      <linearGradient id="footer-fill" x1="0" y1="0" x2="0" y2="1">
        <stop offset="0" stop-color="#2a2a2a"/>
        <stop offset="1" stop-color="#111111"/>
      </linearGradient>
    </defs>
    <path d="M0 0 H939 V455 C800 470 700 440 560 470 C400 505 200 520 0 470 Z" fill="url(#header-fill)"/>
    <path d="M0 478 C200 528 400 512 560 478 C700 448 800 478 939 462 V470 C800 486 700 458 560 490 C400 525 200 540 0 490 Z" fill="#d4d4d4"/>
    <path d="M266 0 H939 V178 C905 198 860 196 830 182 C790 205 730 204 700 186 C650 206 580 204 545 186 C500 205 440 204 405 186 C370 200 320 196 300 176 C280 168 270 150 266 130 Z" fill="var(--cloud)"/>
    <path d="M0 1070 C250 1050 520 1078 720 1070 C820 1066 890 1055 939 1040 V1200 H0 Z" fill="var(--footer-curve)"/>
    <path d="M0 1090 C250 1070 520 1098 720 1090 C820 1086 890 1076 939 1062 V1200 H0 Z" fill="url(#footer-fill)"/>
  </svg>

  <div class="partner-name"><span class="partner-name__mark"></span><span>Harborview<br>University</span></div>

  <h1 class="headline">Reading Skills Classes Online this Summer!</h1>
  <ul class="features features--left">
    <li>Small class size</li>
    <li>A skilled and encouraging teacher</li>
  </ul>
  <ul class="features features--right">
    <li>Individualized skills instruction</li>
    <li>A program of independent</li>
    <li class="features__indent">reading in great books</li>
  </ul>

  <h2 class="skills-title">READING SKILLS:</h2>
  <ul class="skills">
    <li><svg viewBox="0 0 20 20"><path d="M3 10 L8 15 L17 3" fill="none" stroke="#fff" stroke-width="3" stroke-linecap="round" stroke-linejoin="round"/></svg>Phonics</li>
    <li><svg viewBox="0 0 20 20"><path d="M3 10 L8 15 L17 3" fill="none" stroke="#fff" stroke-width="3" stroke-linecap="round" stroke-linejoin="round"/></svg>Comprehension</li>
    <li><svg viewBox="0 0 20 20"><path d="M3 10 L8 15 L17 3" fill="none" stroke="#fff" stroke-width="3" stroke-linecap="round" stroke-linejoin="round"/></svg>Fluency</li>
    <li><svg viewBox="0 0 20 20"><path d="M3 10 L8 15 L17 3" fill="none" stroke="#fff" stroke-width="3" stroke-linecap="round" stroke-linejoin="round"/></svg>Study Skills</li>
    <li><svg viewBox="0 0 20 20"><path d="M3 10 L8 15 L17 3" fill="none" stroke="#fff" stroke-width="3" stroke-linecap="round" stroke-linejoin="round"/></svg>Speed Reading</li>
    <li><svg viewBox="0 0 20 20"><path d="M3 10 L8 15 L17 3" fill="none" stroke="#fff" stroke-width="3" stroke-linecap="round" stroke-linejoin="round"/></svg>Love of Reading</li>
  </ul>

  <div class="photo photo--a" role="img" aria-label="Photo of a young girl reading at home"></div>
  <div class="photo photo--b" role="img" aria-label="Photo of a boy working at a computer"></div>
  <div class="photo photo--c" role="img" aria-label="Photo of a child using a laptop at a desk"></div>
  <div class="photo photo--d" role="img" aria-label="Photo of children reading together on a laptop"></div>

  <div class="monitor">
    <svg width="297" height="263" viewBox="0 0 297 263" aria-hidden="true">
      <rect x="2" y="2" width="293" height="224" rx="8" fill="#2b2b2b" stroke="#9a9a9a" stroke-width="3"/>
      <rect x="12" y="10" width="273" height="206" rx="4" fill="#111"/>
      <circle cx="255" cy="220" r="1.6" fill="#ccc"/><circle cx="262" cy="220" r="1.6" fill="#ccc"/><circle cx="269" cy="220" r="1.6" fill="#ccc"/>
      <path d="M134 226 H163 L168 251 H129 Z" fill="#3a3a3a"/>
      <ellipse cx="148.5" cy="255" rx="52" ry="7" fill="#222"/>
    </svg>
    <div class="monitor__screen" role="img" aria-label="Video class screen showing a teacher presenting a picture book"></div>
  </div>

  <h2 class="programs-title">PROGRAM DESCRIPTIONS:</h2>
  <section class="programs">
    <article class="program">
      <h2>Program for Preschoolers:</h2>
      <p>Students in this program build strong reading readiness skills. Your child will learn letter recognition and beginning phonics, and develop the motivation and love of reading that make learning to read easy, enjoyable, and successful.</p>
    </article>
    <article class="program">
      <h2>Program for Entering Kindergartners:</h2>
      <p>Students in this program learn beginning reading skills and develop a love of books. Your child will learn letter recognition, phonics, and sight words, and will learn to sound out short words.</p>
    </article>
    <article class="program">
      <h2>Program for Entering 1st Graders:</h2>
      <p>Students in this program learn to read independently. Your child will learn phonics and sight words, build comprehension, and gain the skills and confidence needed for success in first grade.</p>
    </article>
    <article class="program">
      <h2>Program for Entering 2nd Graders:</h2>
      <p>Students in this program become fluent, independent readers. Your child will make significant gains in phonics and word-attack skills, fluency, and comprehension, and will develop confidence and a love of reading.</p>
    </article>
    <article class="program">
      <h2>Program for Entering 3rd Graders:</h2>
      <p>Students in this program become strong independent readers. Your child will develop the comprehension, fluency, and long-word decoding skills needed to read longer books with ease, and will build confidence and a love of reading.</p>
    </article>
    <article class="program program--tall">
      <h2>Program for Entering 4th and 5th Graders:</h2>
      <p>Students in this program make substantial gains in comprehension, long-word decoding skills, fluency, and reading speed. Your child will complete homework more quickly and easily, be more successful in school, and become a strong, enthusiastic reader.</p>
    </article>
    <article class="program">
      <h2>Programs for Entering 6th-8th Graders and Entering 9th and 10th Graders:</h2>
      <p>Students in these programs make substantial gains in comprehension while doubling reading speed. They also learn the best way to read textbooks, take notes, and study for tests. As a result, students complete homework more quickly and easily, get better grades, and enjoy reading more.</p>
    </article>
  </section>

  <p class="contact">For More Information or to Register</p>
  <p class="contact__phone">
    <svg viewBox="0 0 24 24" aria-hidden="true"><circle cx="12" cy="12" r="10.5" fill="none" stroke="#fff" stroke-width="1.6"/><path d="M8.2 6.5c.5-.4 1.1-.3 1.4.2l1.1 1.9c.3.5.2 1-.2 1.3l-.8.6c.6 1.5 1.7 2.7 3.1 3.5l.7-.8c.4-.4.9-.5 1.4-.2l1.9 1.1c.5.3.6.9.2 1.4l-.9 1c-.6.6-1.5.8-2.3.5-3.2-1.3-5.6-3.8-6.8-7-.3-.8-.1-1.7.5-2.3z" fill="#fff"/></svg>
    1-800-555-0142
  </p>
  <p class="schedule-note">Please see reverse side for program schedule.</p>
  <p class="hours">Mon.-Fri. 5am–7pm, Sat. 5am–4pm and Sun. 6am–4pm</p>
</main>
</body>
</html>
```